Modern Website Design for PollMeridian – CX & Loyalty SaaS Platform

We need a modern, professional, and responsive website design for our B2B SaaS platform, PollMeridian. We help companies collect real-time customer feedback, analyze insights, and improve loyalty — combining a powerful CX platform with expert consulting services. The website should clearly communicate who we are and what we offer within the first impression. It should balance data-driven visuals such as dashboards, analytics, and charts with a human, approachable feel. The design must include at least six key pages: Homepage, Product/Services, About, Blog/Resources, Contact/Demo, and Pricing. It should be conversion-focused with clear calls-to-action that encourage visitors to request a demo or contact us. The site must be fully responsive across desktop, tablet, and mobile. It should support multiple languages, starting with English and Danish. Most importantly, the delivery must be a final WordPress website, ready to go live, not just design files.

Target Market(s)

Our target market is medium-to-large B2B organizations. The primary audience includes CX leaders, executives, and managers in customer success and service who want to measure loyalty, understand customer insights, and improve retention.

Industry/Entity Type

Technology / SaaS / Customer Experience

Coding

Coded - Design and coding required

Number of Pages Required

5+ page

Font styles to use
Sans Serif

Requirements
Must have
• The project must deliver a final WordPress website that is fully responsive across all devices. The design should be clean, modern, and SaaS-inspired, with clear calls-to-action on every page. It must also support English and Danish, with a visible language toggle. The site should include visuals of dashboards and analytics that reflect data-driven insights. It must feature sections for case studies or testimonials to build trust. The copywriting should be SEO-friendly, and the design should include smooth animations or hover effects that add polish without making the website feel heavy.
Should not have
• Cluttered layouts, or generic stock photos such as handshakes

```html
<!DOCTYPE html>
<html lang="en">
<head>
<meta charset="utf-8">
<title>PollMeridian – Customer Feedback Platform</title>
<link href="https://fonts.googleapis.com/css2?family=Roboto:wght@400;500;700&family=Lato:wght@400;700&display=swap" rel="stylesheet">
<style>
:root{
  --navy:#1b2470;
  --navy-deep:#14164d;
  --blue:#2e4bb8;
  --red:#ef3b24;
  --ink:#1c1d2b;
  --text:#55586a;
  --line:#cfd4ea;
  --soft:#f3f5fb;
  --white:#ffffff;
}
*{margin:0;padding:0;box-sizing:border-box}
html,body{width:1200px;height:4878px;overflow:hidden}
body{position:relative;background:var(--white);font-family:'Lato',sans-serif;color:var(--text)}
.abs{position:absolute}
h1,h2,h3,.heading{font-family:'Roboto',sans-serif;color:var(--ink)}
.btn{position:absolute;display:flex;align-items:center;justify-content:center;border-radius:20px;font-family:'Lato',sans-serif;font-size:12px;font-weight:700}
.btn-red{background:var(--red);color:#fff}
.btn-outline{border:2px solid var(--navy);color:var(--navy);background:#fff}

/* top bar & nav */
.topbar{top:16px;left:0;width:1200px;height:20px;font-size:12px;color:var(--ink)}
.topbar .addr{left:110px}
.topbar .call{left:836px}
.topbar .login{left:1033px}
.icon-red{color:var(--red);margin-right:6px}
.brand{left:110px;top:96px;font-family:'Roboto',sans-serif;font-weight:700;font-size:22px;color:var(--navy);display:flex;align-items:center;gap:8px}
.brand-dot{width:14px;height:14px;border-radius:50%;background:var(--red)}
.nav{top:92px;left:374px;font-size:14px;font-family:'Roboto',sans-serif;color:var(--ink)}
.nav a{color:var(--ink);text-decoration:none;position:absolute;white-space:nowrap}
.nav .active{color:var(--blue);border-bottom:2px solid var(--blue);padding-bottom:4px}

/* hero */
.hero{top:0;left:0;width:1200px;height:645px;background:linear-gradient(180deg,#fff 0%,#f4f6fc 100%)}
.hero-kicker{left:110px;top:294px;font-size:15px;color:var(--blue);font-weight:700}
.hero-title{left:110px;top:322px;font-size:30px;line-height:38px;font-weight:500;color:var(--navy-deep)}
.hero-text{left:110px;top:402px;width:420px;font-size:12px;line-height:24px}
.hero-blob{left:600px;top:190px;width:150px;height:150px;border-radius:50%;background:#eceef4}
.hero-art{left:640px;top:178px;width:420px;height:380px;border-radius:50%;background:radial-gradient(circle at 50% 50%,#dcdee7 0%,#e3e5ec 55%,#eceef4 100%)}
.side-dot{border-radius:50%;background:var(--blue)}

/* contact band */
.contact{top:645px;left:0;width:1200px;height:325px;background:linear-gradient(90deg,#1f3fa0 0%,#1a2a7a 45%,#14164d 100%)}
.notch{left:530px;top:596px;width:140px;height:86px}
.contact h2{position:absolute;top:80px;width:1200px;text-align:center;color:#fff;font-size:32px;font-weight:500}
.field{position:absolute;height:40px;border:1.5px solid rgba(255,255,255,.55);border-radius:20px;background:rgba(255,255,255,.12);color:#fff;font-size:14px;display:flex;align-items:center;padding-left:22px}
.send{position:absolute;height:40px;border-radius:20px;background:#fff;color:var(--navy);font-weight:700;font-size:14px;display:flex;align-items:center;justify-content:center;gap:6px}
.dots{position:absolute;background-image:radial-gradient(circle,rgba(255,255,255,.6) 1.4px,transparent 1.6px);background-size:14px 14px}

/* trusted */
.trusted-title{top:1046px;width:1200px;text-align:center;font-family:'Roboto',sans-serif;font-weight:500;font-size:16px;color:var(--ink);letter-spacing:.3px}
.partner{position:absolute;top:1094px;width:182px;height:82px;border:2px solid #d6dbef;border-radius:8px;display:flex;align-items:center;justify-content:center;background:#fff}
.partner.active{border-color:var(--blue)}
.partner span{display:block;width:70px;height:34px;border-radius:6px;background:#e3e7f4}
.arrow{position:absolute;color:var(--ink);font-size:22px;font-family:'Roboto',sans-serif}

/* how it works */
.section-title{position:absolute;width:1200px;text-align:center;font-family:'Roboto',sans-serif;font-weight:500;font-size:33px;color:var(--ink)}
.how-text{top:1346px;left:180px;width:840px;text-align:center;font-size:13px;line-height:26px}
.laptop{left:218px;top:1477px;width:767px;height:505px;border-radius:22px 22px 0 0;background:#e6e7ec}
.laptop-base{left:128px;top:1982px;width:944px;height:24px;border-radius:0 0 40px 40px;background:linear-gradient(180deg,#e9eaef,#d7d9e0);box-shadow:0 18px 30px rgba(40,50,90,.12)}
.screen{left:251px;top:1510px;width:700px;height:435px;background:#eaaa8a;border:2px solid #d7d8de}
.play{left:533px;top:1660px;width:112px;height:112px;border-radius:50%;background:var(--navy-deep);display:flex;align-items:center;justify-content:center}

/* what we do */
.wwd-bg{top:2118px;width:1200px;text-align:center;font-family:'Roboto',sans-serif;font-size:78px;font-weight:500;color:#eef0f5;letter-spacing:3px}
.service{position:absolute;top:2114px;width:260px;text-align:center}
.service .hex{margin:0 auto;width:88px;height:88px}
.service h3{margin-top:14px;font-size:20px;font-weight:500}
.service p{margin-top:14px;font-size:13px;line-height:26px}

/* about */
.about-ring{left:155px;top:2432px;width:410px;height:410px;border-radius:50%;border:14px solid #e4eef0;background:#fff}
.about-art{left:200px;top:2477px;width:320px;height:320px;border-radius:50%;background:radial-gradient(circle at 50% 55%,#e6e2ee 0%,#f2f1f7 70%)}
.about-blob{left:100px;top:2470px;width:150px;height:150px;border-radius:50%;background:#eef2f2}
.dotgrid{position:absolute;background-image:radial-gradient(circle,#7b80a5 1.3px,transparent 1.5px);background-size:13px 13px}
.about h2{position:absolute;left:636px;top:2456px;font-size:33px;font-weight:500}
.about p{position:absolute;left:636px;width:420px;font-size:13px;line-height:24px}
.about-arc{left:860px;top:2620px;width:520px;height:520px;border-radius:50%;border:12px solid #eef0f8}

/* testimonials */
.tcard{position:absolute;top:3040px;height:301px;border-radius:8px;background:#f4f5fc;padding:38px 36px}
.tcard.active{border:2.5px solid var(--navy-deep);background:#fff}
.tcard .quote{position:absolute;left:32px;top:16px;font-family:'Roboto',sans-serif;font-size:80px;line-height:80px;color:#e4e7f2}
.tcard h3{position:relative;font-size:19px;font-weight:500;color:var(--navy-deep)}
.tcard p{position:relative;margin-top:16px;font-size:12.5px;line-height:26px}
.person{position:absolute;left:34px;top:212px;display:flex;align-items:center;gap:14px}
.avatar{width:60px;height:60px;border-radius:50%;background:#e9e3df;border:3px solid #d7dcef}
.person b{display:block;font-size:15px;color:var(--ink);font-weight:400}
.person small{font-size:11px}

/* cta */
.cta{left:112px;top:3479px;width:976px;height:224px;border-radius:112px;background:linear-gradient(90deg,#1f3fa0 0%,#1a2477 55%,#14164d 100%)}
.cta h2{position:absolute;top:54px;width:976px;text-align:center;color:#fff;font-size:33px;line-height:43px;font-weight:500}

/* faq */
.faq-art{left:114px;top:3881px;width:406px;height:454px;border-radius:40% 40% 10% 10%;background:linear-gradient(180deg,#f1f2f8 0%,#e4e6f0 100%)}
.faq-item{position:absolute;left:532px;width:558px;height:56px;border:1.5px solid #d5d9ea;border-radius:28px;background:#fff;display:flex;align-items:center;font-size:13px;color:var(--ink)}
.faq-item.open{border:2.5px solid var(--blue)}
.faq-num{width:34px;height:34px;border-radius:50%;border:2px solid var(--blue);color:var(--navy);display:flex;align-items:center;justify-content:center;font-size:13px;font-weight:700;margin-left:-2px;margin-right:16px;flex:none;background:#fff}
.faq-q{flex:1;line-height:20px}
.faq-plus{width:40px;color:var(--navy);font-size:24px;text-align:center;font-family:'Roboto',sans-serif}

/* footer */
.footer{top:4411px;left:0;width:1200px;height:360px;background:#f3f5fc}
.fcol{position:absolute;top:4472px}
.fcol h3{font-size:20px;font-weight:500;border-left:3px solid var(--red);padding-left:22px;line-height:20px}
.fcol ul{list-style:none;margin-top:18px;padding-left:25px;font-size:15px;line-height:26px;color:var(--ink)}
.subscribe-label{left:172px;top:4670px;font-size:20px;color:var(--ink)}
.subscribe-label em{font-style:normal;color:var(--blue)}
.subscribe{left:583px;top:4658px;width:446px;height:50px;border:1.5px solid #d2d6e8;border-radius:25px;background:#fff;display:flex;align-items:center;padding-left:36px;font-size:12px;color:var(--ink)}
.subscribe-btn{left:976px;top:4664px;width:40px;height:40px;border-radius:50%;background:var(--navy-deep);display:flex;align-items:center;justify-content:center}
.copyright{top:4770px;left:0;width:1200px;height:108px;background:#f7f8fd;border-top:1px solid #e6e8f2}
.copyright p{position:absolute;top:44px;width:1200px;text-align:center;font-size:15px;color:var(--ink)}
.copyright a{color:var(--blue)}
</style>
</head>
<body>

<!-- HERO -->
<section class="hero abs">
  <div class="topbar abs">
    <span class="abs addr"><span class="icon-red">&#9679;</span>123, Lorem ipsum dolor sit amet</span>
    <span class="abs call"><span class="icon-red">&#9742;</span>Call : +1 555 014 2277</span>
    <span class="abs login"><span class="icon-red">&#9679;</span>Log in</span>
  </div>

  <div class="brand abs"><span class="brand-dot"></span>PollMeridian</div>

  <nav class="nav abs">
    <a class="active" style="left:0">Home</a>
    <a style="left:80px">Product/Services</a>
    <a style="left:242px">About</a>
    <a style="left:323px">Blog</a>
    <a style="left:393px">Pricing</a>
    <a style="left:480px">Contact</a>
  </nav>
  <div class="btn btn-red" style="left:964px;top:84px;width:124px;height:34px">Book a Demo</div>

  <div class="hero-blob abs"></div>
  <div class="hero-art abs" role="img" aria-label="Illustration of a woman placing a star on a customer rating board beside a feedback checklist"></div>
  <div class="dotgrid" style="left:646px;top:380px;width:44px;height:150px"></div>

  <div class="hero-kicker abs">PollMeridian</div>
  <h1 class="hero-title abs">Turn Customer Feedback Into<br>Measurable Business Growth</h1>
  <p class="hero-text abs">Lorem ipsum dolor sit amet, consectetur adipiscing elit, sed do tempor incididunt ut labore et dolore magna aliqua.</p>
  <div class="btn btn-red" style="left:110px;top:467px;width:124px;height:32px">Book a Demo</div>
  <div class="btn btn-outline" style="left:242px;top:467px;width:148px;height:32px">Start a Free Trial</div>

  <div class="side-dot abs" style="left:-12px;top:258px;width:26px;height:26px"></div>
  <div class="side-dot abs" style="left:1186px;top:566px;width:26px;height:26px;background:var(--navy-deep)"></div>
</section>

<!-- CONTACT BAND -->
<section class="contact abs">
  <div class="dots" style="left:0;top:92px;width:76px;height:150px"></div>
  <div class="dots" style="left:1124px;top:92px;width:76px;height:150px"></div>
  <h2>Get in touch</h2>
  <div class="field" style="left:150px;top:144px;width:293px">Name</div>
  <div class="field" style="left:454px;top:144px;width:294px">Email</div>
  <div class="field" style="left:757px;top:144px;width:294px">Phone</div>
  <div class="field" style="left:150px;top:199px;width:598px">Message</div>
  <div class="send" style="left:757px;top:199px;width:294px">Send Message
    <svg width="14" height="14" viewBox="0 0 24 24"><path d="M2 12 22 3 15 22 11 13z" fill="currentColor"/></svg>
  </div>
</section>
<svg class="notch abs" viewBox="0 0 140 86" aria-hidden="true">
  <path d="M0 49 C30 49 40 86 70 86 C100 86 110 49 140 49 L140 0 L0 0Z" fill="#f4f6fc"/>
  <path d="M70 30 L70 56 M62 48 L70 56 L78 48" stroke="#2e4bb8" stroke-width="2.5" fill="none"/>
  <text x="70" y="18" text-anchor="middle" font-size="7" fill="#1c1d2b" font-family="Lato,sans-serif" letter-spacing="1.5">SCROLL DOWN</text>
</svg>

<!-- TRUSTED -->
<div class="trusted-title abs">TRUSTED BY HUNDREDS OF COMPANIES WORLDWIDE</div>
<div class="arrow" style="left:44px;top:1120px">&#8249;</div>
<div class="partner" style="left:110px"><span></span></div>
<div class="partner" style="left:310px"><span></span></div>
<div class="partner active" style="left:510px"><span></span></div>
<div class="partner" style="left:709px"><span></span></div>
<div class="partner" style="left:908px"><span></span></div>
<div class="arrow" style="left:1137px;top:1120px">&#8250;</div>

<!-- HOW IT WORKS -->
<h2 class="section-title" style="top:1288px">How It Works</h2>
<p class="how-text abs">Lorem ipsum dolor sit amet, consectetur adipiscing elit, sed do eiusmod tempor incididunt ut labore et dolore magna aliqua. Ut enim ad minim veniam, quis nostrud exercitation ullamco laboris nisi ut aliquip ex ea commodo consequat.</p>
<div class="btn btn-red" style="left:517px;top:1410px;width:166px;height:32px">Start a Free Trial</div>

<div class="laptop abs"></div>
<div class="laptop-base abs"></div>
<div class="screen abs" role="img" aria-label="Video still of a team holding stars beneath rating speech bubbles"></div>
<div class="play abs"><svg width="40" height="40" viewBox="0 0 24 24"><path d="M7 4 20 12 7 20z" fill="#fff"/></svg></div>

<!-- WHAT WE DO -->
<div class="wwd-bg abs">WHAT WE DO</div>
<div class="service" style="left:144px">
  <svg class="hex" viewBox="0 0 88 88"><path d="M44 3 80 23 80 65 44 85 8 65 8 23Z" fill="#fff" stroke="#2e4bb8" stroke-width="2"/><circle cx="44" cy="42" r="12" fill="none" stroke="#1b2470" stroke-width="2"/><path d="M28 60h32" stroke="#1b2470" stroke-width="2"/></svg>
  <h3>Lorem ipsum dolor</h3>
  <p>Lorem ipsum dolor sit amet, conse ctetur adipiscing elit, sed do eiusmod tempor incididunt</p>
</div>
<div class="service" style="left:470px">
  <svg class="hex" viewBox="0 0 88 88"><path d="M44 3 80 23 80 65 44 85 8 65 8 23Z" fill="#fff" stroke="#2e4bb8" stroke-width="2"/><circle cx="44" cy="38" r="10" fill="none" stroke="#1b2470" stroke-width="2"/><path d="M26 56q18 10 36 0" stroke="#1b2470" stroke-width="2" fill="none"/></svg>
  <h3>Lorem ipsum dolor</h3>
  <p>Lorem ipsum dolor sit amet, conse ctetur adipiscing elit, sed do eiusmod tempor incididunt</p>
</div>
<div class="service" style="left:796px">
  <svg class="hex" viewBox="0 0 88 88"><path d="M44 3 80 23 80 65 44 85 8 65 8 23Z" fill="#fff" stroke="#2e4bb8" stroke-width="2"/><circle cx="40" cy="42" r="11" fill="none" stroke="#1b2470" stroke-width="2"/><circle cx="54" cy="50" r="7" fill="none" stroke="#1b2470" stroke-width="2"/></svg>
  <h3>Lorem ipsum dolor</h3>
  <p>Lorem ipsum dolor sit amet, conse ctetur adipiscing elit, sed do eiusmod tempor incididunt</p>
</div>
<div class="abs" style="left:1186px;top:2180px;width:0;height:0;border-top:14px solid transparent;border-bottom:14px solid transparent;border-right:16px solid var(--blue)"></div>

<!-- ABOUT -->
<section class="about">
  <div class="about-arc abs"></div>
  <div class="about-blob abs"></div>
  <div class="dotgrid" style="left:124px;top:2674px;width:150px;height:152px"></div>
  <div class="about-ring abs"></div>
  <div class="about-art abs" role="img" aria-label="Illustration of two people rating a feedback form on a large screen"></div>
  <h2>About Us</h2>
  <p style="top:2512px">PollMeridian is a B2B customer experience (CX) and loyalty platform combined with expert consulting services. We collect real-time feedback, segment insights, and provide leadership-ready reporting with churn-risk alerts. Unlike software-only tools, our platform includes CX experts who help businesses implement, interpret, and act on insights.</p>
  <p style="top:2680px">Our target audience is HR leaders, CX leaders, executives, and managers at medium-to-large organizations who want to improve customer loyalty, strengthen relationships, and drive measurable results.</p>
  <div class="btn btn-red" style="left:636px;top:2796px;width:126px;height:32px">Learn more</div>
</section>

<!-- TESTIMONIALS -->
<h2 class="section-title" style="top:2966px">What Customer Says</h2>
<div class="arrow" style="left:44px;top:3164px">&#8249;</div>
<div class="tcard active" style="left:110px;width:471px">
  <div class="quote">&ldquo;</div>
  <h3>Lorem ipsum dolor sit amet, consec</h3>
  <p>Lorem ipsum dolor sit amet, consectetur adipiscing elit, sed do eiusmod tempor incididunt ut labore et dolore magna aliqua. Ut enim ad minim veniam, quis nostrud exercitation ullamco laboris nisi ut aliquip ex ea commodo</p>
  <div class="person"><div class="avatar" role="img" aria-label="Portrait of Martin L."></div><div><b>Martin L.</b><small>Company name</small></div></div>
</div>
<div class="tcard" style="left:619px;width:469px">
  <div class="quote">&ldquo;</div>
  <h3>Lorem ipsum dolor sit amet, consec</h3>
  <p>Lorem ipsum dolor sit amet, consectetur adipiscing elit, sed do eiusmod tempor incididunt ut labore et dolore magna aliqua. Ut enim ad minim veniam, quis nostrud exercitation ullamco laboris nisi ut aliquip ex ea commodo</p>
  <div class="person"><div class="avatar" role="img" aria-label="Portrait of Oliver K."></div><div><b>Oliver K.</b><small>Company name</small></div></div>
</div>
<div class="arrow" style="left:1137px;top:3164px">&#8250;</div>

<!-- CTA -->
<section class="cta abs">
  <h2>Ready to Strengthen Your Customer<br>Relationships?</h2>
  <div class="btn btn-red" style="left:416px;top:150px;width:144px;height:32px">Start Free Trial</div>
</section>

<!-- FAQ -->
<h2 class="section-title" style="top:3818px">Frequently Asked Question</h2>
<div class="faq-art abs" role="img" aria-label="Illustration of a large question mark with star ratings and a woman holding a star"></div>
<div class="abs" style="left:0;top:4010px;width:0;height:0;border-top:34px solid transparent;border-bottom:34px solid transparent;border-left:34px solid var(--navy-deep)"></div>

<div class="faq-item open" style="top:3894px"><div class="faq-num">1</div><div class="faq-q">Is FeedbackFlow easy to use, even for non-technical users?</div><div class="faq-plus">+</div></div>
<div class="faq-item" style="top:3962px"><div class="faq-num">2</div><div class="faq-q">How long does it take to implement FeedbackFlow?</div><div class="faq-plus">+</div></div>
<div class="faq-item" style="top:4031px"><div class="faq-num">3</div><div class="faq-q">Does FeedbackFlow cover the full Purchase-To-Pay process?</div><div class="faq-plus">+</div></div>
<div class="faq-item" style="top:4099px"><div class="faq-num">4</div><div class="faq-q">What kind of training and onboarding support does<br>FeedbackFlow provide?</div><div class="faq-plus">+</div></div>
<div class="faq-item" style="top:4168px"><div class="faq-num">5</div><div class="faq-q">What is the setup and implementation cost?</div><div class="faq-plus">+</div></div>
<div class="faq-item" style="top:4236px"><div class="faq-num">6</div><div class="faq-q">What can I expect from the FeedbackFlow demo?</div><div class="faq-plus">+</div></div>

<!-- FOOTER -->
<footer>
  <div class="footer abs"></div>
  <div class="fcol" style="left:110px"><h3>Product</h3><ul><li>Solutions</li><li>Features</li><li>Integrations</li><li>Pricing</li></ul></div>
  <div class="fcol" style="left:377px"><h3>Company</h3><ul><li>About us</li><li>Partners and affiliates</li><li>Blog</li><li>Contact</li></ul></div>
  <div class="fcol" style="left:668px"><h3>Support</h3><ul><li>FAQs</li><li>Contact</li><li>Book a Demo</li><li>Partners</li></ul></div>
  <div class="fcol" style="left:958px"><h3>Links</h3><ul><li>Blog</li><li>About</li><li>Careers</li><li>Press</li></ul></div>

  <div class="subscribe-label abs">Subscribe to the <em>PollMeridian</em> newsletter</div>
  <div class="subscribe abs">Email address</div>
  <div class="subscribe-btn abs"><svg width="16" height="16" viewBox="0 0 24 24"><path d="M2 12 22 3 15 22 11 13z" fill="#fff"/></svg></div>

  <div class="copyright abs"><p>Copyright @ 2025 <a>PollMeridian</a>. All Rights Reserved</p></div>
</footer>

</body>
</html>
```